Develop a PowerPoint template based on existing logo for a non-profit international alliance of professionals.
Presentations that will be made with this template will include mostly bullet point text and some tables. SOme images could also be included.

Target Market(s)

Governments, private funders

Industry/Entity Type

Non-Profit

Requirements
Must have
• clean and modern feel
Should not have
• no background in the slide area

```html
<!DOCTYPE html>
<html lang="en">
<head>
<meta charset="utf-8">
<title>Global Innovation Partnership – Presentation Template</title>
<link href="https://fonts.googleapis.com/css2?family=Nunito:wght@800&family=Oswald:wght@400&family=Tinos:wght@400;700&display=swap" rel="stylesheet">
<style>
  :root {
    --stage: #4a4a4a;
    --slide: #f1f1f2;
    --slide-edge: #e4e4e6;
    --brand-red: #e3161f;
    --band-dark: #c40f17;
    --ink: #1e1e1e;
    --body-ink: #333333;
    --rule: #bdbdbd;
    --footer-ink: #555555;
  }
  * { margin: 0; padding: 0; box-sizing: border-box; }
  html, body { width: 1200px; height: 808px; overflow: hidden; }
  body { background: var(--stage); position: relative; font-family: "Tinos", "Times New Roman", serif; }

  .slide {
    position: absolute;
    width: 533px;
    height: 372px;
    background: linear-gradient(180deg, #fafafa 0%, var(--slide) 70%, var(--slide-edge) 100%);
    overflow: hidden;
  }
  .slide--title   { left: 55px;  top: 22px; }
  .slide--content { left: 620px; top: 18px; }
  .slide--media   { left: 55px;  top: 420px; }
  .slide--closing { left: 620px; top: 420px; height: 376px; }

  .brand-band {
    position: absolute; left: 0; right: 0;
    background: linear-gradient(180deg, var(--brand-red), var(--band-dark));
    display: flex; align-items: center; justify-content: center; gap: 8px;
  }
  .brand-band__dot { width: 14px; height: 14px; border-radius: 50%; background: #ffffff; }
  .brand-band__name {
    font-family: "Oswald", "Arial Narrow", sans-serif; font-weight: 400;
    color: #ffffff; font-size: 13px; letter-spacing: 1px;
  }
  .slide--title .brand-band { top: 316px; height: 32px; }
  .slide--title .base-strip { position: absolute; left: 0; right: 0; top: 348px; bottom: 0; background: linear-gradient(180deg, #d2d2d4, #e8e8ea); }

  .accent-bar { position: absolute; left: 0; right: 0; bottom: 0; height: 16px; background: linear-gradient(180deg, var(--brand-red), var(--band-dark)); }

  .hero-mark { position: absolute; width: 110px; height: 110px; border-radius: 50%; background: var(--brand-red); }
  .slide--title .hero-mark { left: 212px; top: 68px; }
  .slide--closing .hero-mark { left: 214px; top: 66px; }

  .headline {
    position: absolute; left: 0; right: 0; text-align: center;
    font-family: "Nunito", "Century Gothic", sans-serif; font-weight: 800;
    color: var(--brand-red); font-size: 28px; line-height: 1;
  }
  .subline {
    position: absolute; left: 0; right: 0; text-align: center;
    font-family: "Nunito", "Century Gothic", sans-serif; font-weight: 800;
    color: var(--ink); font-size: 18px; line-height: 1;
  }
  .slide--title .headline { top: 234px; }
  .slide--title .subline { top: 266px; }
  .slide--closing .headline { top: 220px; }
  .slide--closing .subline { top: 252px; }

  .corner-brand { position: absolute; display: flex; align-items: center; gap: 6px; }
  .corner-brand__dot { width: 16px; height: 16px; border-radius: 50%; background: var(--brand-red); }
  .corner-brand__name {
    font-family: "Oswald", "Arial Narrow", sans-serif; font-weight: 400;
    color: var(--brand-red); font-size: 11px; line-height: 1.05; letter-spacing: .5px;
    text-transform: uppercase; padding-left: 6px; border-left: 1px solid var(--rule);
  }
  .slide--content .corner-brand { left: 52px; top: 40px; }
  .slide--media .corner-brand { left: 51px; top: 38px; }

  .section-heading { position: absolute; font-weight: 700; font-size: 14px; color: var(--brand-red); }
  .body-copy { position: absolute; font-size: 9px; line-height: 11.5px; color: var(--body-ink); }
  .divider { position: absolute; width: 1px; background: linear-gradient(180deg, transparent, #8a8a8a, transparent); }

  .bullet-list { position: absolute; left: 323px; top: 143px; list-style: none; }
  .bullet-list li { display: flex; align-items: center; gap: 7px; font-size: 9px; color: var(--body-ink); height: 22.5px; }
  .bullet-list li::before { content: ""; width: 9px; height: 9px; border-radius: 50%; background: var(--brand-red); }

  .image-slot {
    position: absolute; left: 51px; top: 135px; width: 198px; height: 94px;
    border: 2px solid #d8d8d8;
    background: radial-gradient(circle at 50% 45%, #ffffff 0%, #e6e6e6 55%, #d9d9d9 100%);
  }
  .body-copy--long { line-height: 19px; text-align: justify; }

  .slide--closing .brand-band { top: 286px; height: 36px; }
  .contact-block {
    position: absolute; left: 0; right: 0; top: 322px; bottom: 0;
    background: linear-gradient(180deg, #d6d6d8, #ececee);
    text-align: center; padding-top: 16px;
    font-family: "Oswald", "Arial Narrow", sans-serif; font-size: 7px; line-height: 9px; color: var(--footer-ink);
  }
  .contact-block svg { vertical-align: -1px; margin-right: 2px; }
</style>
</head>
<body>

  <section class="slide slide--title">
    <div class="hero-mark"></div>
    <h1 class="headline">Your Title Goes Here</h1>
    <p class="subline">Subtitle Goes Here</p>
    <div class="brand-band">
      <span class="brand-band__dot"></span>
      <span class="brand-band__name">GIP | GLOBAL INNOVATION PARTNERSHIP</span>
    </div>
    <div class="base-strip"></div>
  </section>

  <section class="slide slide--content">
    <div class="corner-brand">
      <span class="corner-brand__dot"></span>
      <span class="corner-brand__name">Global<br>Innovation<br>Partnership</span>
    </div>
    <h2 class="section-heading" style="left:53px;top:112px;">Heading 1</h2>
    <p class="body-copy" style="left:53px;top:135px;width:200px;">Lorem Ipsum is simply dummy text of the printing and typesetting industry. Lorem Ipsum has been the industry's standard dummy text ever since the 1500s, when an unknown printer took a galley of type and scrambled it to make a type specimen book.</p>
    <h2 class="section-heading" style="left:53px;top:211px;">Heading 2</h2>
    <p class="body-copy" style="left:53px;top:234px;width:200px;">Lorem Ipsum is simply dummy text of the printing and typesetting industry. Lorem Ipsum has been the industry's standard dummy text ever since the 1500s, when an unknown printer took a galley of type and scrambled it to make a type specimen book.</p>
    <div class="divider" style="left:281px;top:110px;height:190px;"></div>
    <h2 class="section-heading" style="left:308px;top:112px;">Heading 3</h2>
    <ul class="bullet-list">
      <li>Lorem Ipsum is simply dummy text.</li>
      <li>Lorem Ipsum is simply dummy text.</li>
      <li>Lorem Ipsum is simply dummy text.</li>
      <li>Lorem Ipsum is simply dummy text.</li>
      <li>Lorem Ipsum is simply dummy text.</li>
      <li>Lorem Ipsum is simply dummy text.</li>
      <li>Lorem Ipsum is simply dummy text.</li>
    </ul>
    <div class="accent-bar"></div>
  </section>

  <section class="slide slide--media">
    <div class="corner-brand">
      <span class="corner-brand__dot"></span>
      <span class="corner-brand__name">Global<br>Innovation<br>Partnership</span>
    </div>
    <h2 class="section-heading" style="left:51px;top:113px;">Heading 4</h2>
    <div class="image-slot" role="img" aria-label="Image placeholder for a supporting photo"></div>
    <p class="body-copy" style="left:51px;top:237px;width:200px;">Lorem Ipsum is simply dummy text of the printing and typesetting industry. Lorem Ipsum has been the industry's standard dummy text ever since the 1500s, when an unknown printer took a galley of type and scrambled it to make a type specimen book.</p>
    <div class="divider" style="left:268px;top:110px;height:190px;"></div>
    <h2 class="section-heading" style="left:283px;top:113px;">Heading 5</h2>
    <p class="body-copy body-copy--long" style="left:283px;top:132px;width:200px;">Lorem Ipsum is simply dummy text of the printing and typesetting industry. Lorem Ipsum has been the industry's standard dummy text ever since the 1500s, when an unknown printer took a galley of type and scrambled it to make a type specimen book. It has survived not only five centuries, but also the leap into electronic typesetting, remaining essentially unchanged. It was popularised in the 1960s with the release of Letraset sheets containing Lorem Ipsum passages, and more recently with desktop publishing software like Aldus PageMaker including versions of Lorem Ipsum.</p>
    <div class="accent-bar"></div>
  </section>

  <section class="slide slide--closing">
    <div class="hero-mark"></div>
    <h1 class="headline">Thank you very much</h1>
    <p class="subline">for your valueable time</p>
    <div class="brand-band">
      <span class="brand-band__dot"></span>
      <span class="brand-band__name">GIP | GLOBAL INNOVATION PARTNERSHIP</span>
    </div>
    <div class="contact-block">
      <p>Level 9, 120 Harbour Rd, Eastport 4100</p>
      <p>
        <svg width="7" height="6" viewBox="0 0 7 6"><path d="M0 2 Q3.5 -1 7 2 L6 3 L5 2 L2 2 L1 3 Z M1.5 3 H5.5 V6 H1.5 Z" fill="#e3161f"/></svg>02 5550 1234
        <svg width="7" height="6" viewBox="0 0 7 6"><path d="M0 2 Q3.5 -1 7 2 L6 3 L5 2 L2 2 L1 3 Z M1.5 3 H5.5 V6 H1.5 Z" fill="#e3161f"/></svg>02 5550 5678
      </p>
      <p>
        <svg width="7" height="5" viewBox="0 0 7 5"><rect width="7" height="5" fill="#e3161f"/><path d="M0 0 L3.5 3 L7 0" stroke="#fff" stroke-width=".8" fill="none"/></svg>info@gipalliance.org
      </p>
    </div>
  </section>

</body>
</html>
```